Family Owned Construction Company Needs Modern Business Cards

We need a new design for our business cards. We are a family owned construction company, Brantwell Construction, based in Mendon, Vermont and would like to add in our new logo and find a more modern look. We also want to use our old to make sure people know who we are. We do site development, highway, environmental, demolition, utility and aggregate.

Contact Information for Business Card

We want to have the office address, 418 Quarry Ridge Road, Alderbrook, XN 05788 and our phone (802) 555-0137 and fax (802) 555-0164 on there as well. Our website is www.brantwellinc.example. There should be a place for the person's name, title, cell number, and email address on the card. Words that we would like to be associated with our company are honesty, predictable, reliable, integrity, dedicated, built right quality, consistent, whatever it takes, and innovation. Safety is also very important to us.

Font styles to use
Serif
Sans Serif
Other font styles liked:
• Square 721 Extented

Colors
0255a3
ffffff

Requirements
Must have
• Office address, phone number and fax number. New logo with excavator
Nice to have
• That we do site development, highway, environmental, demolition, utility, and aggregate. Both logos

```html
<!DOCTYPE html>
<html lang="en">
<head>
<meta charset="utf-8">
<title>Brantwell Construction Business Cards</title>
<link href="https://fonts.googleapis.com/css2?family=Arimo:wght@400;700&display=swap" rel="stylesheet">
<style>
  :root {
    --navy: #22366b;
    --navy-soft: #3b4f85;
    --paper: #ffffff;
    --backdrop: #2b2b2d;
  }
  * { box-sizing: border-box; margin: 0; padding: 0; }
  html, body {
    width: 1200px; height: 880px; overflow: hidden;
    background: var(--backdrop);
    font-family: "Arimo", Arial, sans-serif;
    color: var(--navy);
  }
  .sheet {
    width: 1200px; height: 880px;
    display: flex; align-items: center; justify-content: center; gap: 40px;
  }
  .card {
    position: relative;
    width: 560px; height: 320px;
    background: var(--paper);
    border-radius: 22px;
    overflow: hidden;
  }
  /* front */
  .card--front .brand-mark {
    position: absolute; left: 0; right: 0; top: 95px;
    display: flex; align-items: center; justify-content: center; gap: 12px;
  }
  .brand-square {
    width: 34px; height: 34px; background: var(--navy);
  }
  .brand-name {
    font-weight: 700; font-size: 26px; color: var(--navy); letter-spacing: 0.5px;
    white-space: nowrap;
  }
  .services {
    position: absolute; left: 0; right: 0; bottom: 52px;
    text-align: center; font-size: 17px; line-height: 1.3; color: var(--navy);
  }
  .services .sep { margin: 0 6px; }
  /* back */
  .back-brand {
    position: absolute; left: 34px; top: 42px; width: 250px;
  }
  .card--back .brand-name { font-size: 21px; letter-spacing: 0; }
  .contact {
    position: absolute; left: 34px; top: 112px; width: 250px;
    font-size: 15px; line-height: 1.25;
  }
  .person-name { font-weight: 700; font-size: 20px; text-transform: uppercase; }
  .person-title { font-size: 15px; margin-bottom: 12px; }
  .address { margin-bottom: 8px; }
  .phone-line { display: flex; align-items: center; gap: 7px; }
  .phone-line svg { width: 17px; height: 17px; flex: none; }
  .website { margin-top: 10px; font-size: 14px; white-space: nowrap; }
  .website b { font-weight: 700; }
  .excavator-art {
    position: absolute; right: 0; top: 0;
    width: 250px; height: 320px;
    background: linear-gradient(160deg, var(--navy) 0%, var(--navy-soft) 60%, #dfe3ee 100%);
  }
</style>
</head>
<body>
<main class="sheet">
  <section class="card card--front">
    <div class="brand-mark">
      <span class="brand-square"></span>
      <span class="brand-name">Brantwell Construction</span>
    </div>
    <p class="services">
      site<span class="sep">|</span>heavy highway<span class="sep">|</span>environmental<span class="sep">|</span>demolition<span class="sep">|</span>utilities<br>aggregate
    </p>
  </section>

  <section class="card card--back">
    <div class="back-brand">
      <span class="brand-name">Brantwell Construction</span>
    </div>
    <div class="contact">
      <p class="person-name">Dana Whitcomb</p>
      <p class="person-title">Managing Director</p>
      <p class="address">418 Quarry Ridge Road,<br>Alderbrook, XN 05788</p>
      <p class="phone-line">
        <svg viewBox="0 0 20 20"><circle cx="10" cy="10" r="10" fill="var(--navy)"/><path d="M6.5 5.5l2 0 .8 2.4-1.3.9a7 7 0 0 0 3.2 3.2l.9-1.3 2.4.8v2a1 1 0 0 1-1 1A8.5 8.5 0 0 1 5.5 6.5a1 1 0 0 1 1-1z" fill="#fff"/></svg>
        (802) 555-0137
      </p>
      <p class="phone-line">
        <svg viewBox="0 0 20 20"><circle cx="10" cy="10" r="10" fill="var(--navy)"/><rect x="6" y="5" width="8" height="4" fill="#fff"/><rect x="5" y="9" width="10" height="5" rx="1" fill="#fff"/><rect x="7" y="12" width="6" height="3" fill="var(--navy)"/></svg>
        (802) 555-0164
      </p>
      <p class="website">www.<b>brantwellinc</b>.example</p>
    </div>
    <div class="excavator-art" role="img" aria-label="Large excavator arm and bucket illustration"></div>
  </section>
</main>
</body>
</html>
```